Criação de Layout Web-Design para Contabilidade & Finanças
A empresa queria:
" A Orvalis é um HUB financeiro para o cliente. Através da Orvalis, o cliente tem acesso a serviços de Investimentos (Orvalis Investimentos), Crédito (Orvalis Crédito), Seguros (Orvalis Seguros), Câmbio, Consultoria Financeira, Tributária, Patrimonial, Jurídica etc. Funciona como um "family office" voltado a atender com excelência e assertividade as demandas de um cliente de alto patrimônio. Isso é possível graças a uma extensa e qualificada rede de parceiros. A Orvalis foca em investimentos e os parceiros focam nas outras demandas. "

```html
<!DOCTYPE html>
<html lang="pt-BR">
<head>
<meta charset="UTF-8">
<title>Orvalis — Hub Financeiro</title>
<link href="https://fonts.googleapis.com/css2?family=Montserrat:wght@400;500;600&family=Open+Sans:wght@400;600&display=swap" rel="stylesheet">
<style>
  :root {
    --page: #ffffff;
    --ink: #3a3d42;
    --body-ink: #4a4d52;
    --nav-ink: #ffffff;
    --navy-1: #1f2a3a;
    --navy-2: #3a4a60;
    --band-ink: #e6ebf2;
    --brand-ink: #d9dde3;
    --photo-light: #eef0f2;
    --photo-mid: #d6dbe0;
    --photo-dark: #9aa3ad;
  }
  * { margin: 0; padding: 0; box-sizing: border-box; }
  html, body { width: 1200px; height: 1200px; overflow: hidden; background: var(--page); }
  body { position: relative; font-family: "Open Sans", Arial, sans-serif; }

  .hero {
    position: absolute; left: 48px; top: 0; width: 1104px; height: 547px;
    background: linear-gradient(180deg, #a7adb4 0%, #d3d7dc 22%, var(--photo-light) 55%, #f6f7f8 100%);
  }
  .hero-photo {
    position: absolute; inset: 0;
    background: radial-gradient(ellipse at 30% 45%, rgba(200,190,180,0.45) 0%, rgba(255,255,255,0) 45%),
                radial-gradient(ellipse at 85% 40%, rgba(150,165,185,0.35) 0%, rgba(255,255,255,0) 40%);
  }
  .brand {
    position: absolute; left: 72px; top: 40px;
    display: flex; align-items: center; gap: 14px;
    font-family: "Montserrat", sans-serif; font-weight: 600; font-size: 46px;
    letter-spacing: 4px; color: var(--brand-ink); text-transform: uppercase;
  }
  .brand-dot { width: 14px; height: 14px; border-radius: 50%; background: var(--brand-ink); }
  .nav {
    position: absolute; right: 52px; top: 66px;
    display: flex; gap: 10px; list-style: none;
    font-family: "Montserrat", sans-serif; font-size: 15px; font-weight: 500;
    color: var(--nav-ink); text-transform: uppercase; letter-spacing: 0.3px;
  }
  .nav li + li::before { content: "|"; margin-right: 10px; }
  .nav .active { font-weight: 600; }
  .hero-title {
    position: absolute; left: 72px; top: 372px;
    font-family: "Montserrat", sans-serif; font-weight: 400; font-size: 41px;
    line-height: 54px; color: var(--ink);
  }

  .section-band {
    position: absolute; left: 48px; top: 547px; width: 1104px; height: 53px;
    background: linear-gradient(90deg, var(--navy-1), var(--navy-2) 60%, var(--navy-1));
    color: var(--band-ink); font-family: "Montserrat", sans-serif;
    font-size: 14px; font-weight: 600; letter-spacing: 0.5px;
    display: flex; align-items: center; padding-left: 36px;
  }

  .about-text {
    position: absolute; left: 84px; top: 650px; width: 560px;
    font-size: 16.5px; line-height: 32px; color: var(--body-ink);
  }

  .brand-panel {
    position: absolute; left: 48px; top: 1003px; width: 595px; height: 197px;
    background: linear-gradient(180deg, var(--navy-2), var(--navy-1));
    display: flex; align-items: center; justify-content: center;
  }
  .brand-panel .brand { position: static; font-size: 50px; }

  .about-photo {
    position: absolute; left: 643px; top: 600px; width: 509px; height: 600px;
    background: linear-gradient(160deg, #f2f4f6 0%, var(--photo-mid) 45%, #4b5360 80%, #2e333b 100%);
  }
</style>
</head>
<body>
  <header class="hero">
    <div class="hero-photo" role="img" aria-label="Fotografia de dois profissionais trabalhando juntos em um escritório claro"></div>
    <div class="brand"><span class="brand-dot"></span>Orvalis</div>
    <ul class="nav">
      <li class="active">Home</li>
      <li>Quem Somos</li>
      <li>Serviços</li>
      <li>Portfólio</li>
      <li>Contato</li>
    </ul>
    <h1 class="hero-title">Inteligência em Investimentos<br>e Serviços Financeiros</h1>
  </header>

  <div class="section-band">:: QUEM SOMOS</div>

  <p class="about-text">
    A Orvalis é uma corretora especializada em seguro de crédito para<br>
    grandes empresas bancos e instituições financeiras.<br>
    Nossa missão é oferecer um serviço diferenciado, entendendo o perfil<br>
    de cada cliente para oferecer soluções inovadoras e criativas em<br>
    seguros de crédito, bem como serviços exclusivos e de alto padrão.<br>
    A Orvalis começa sua história no ano de 2019, acreditando que manter<br>
    a qualidade com foco no cliente, sempre mantendo<br>
    um atendimento diferenciado e personalizado é um diferencial.<br>
    Na visão da empresa e de seu fundador a qualidade e o atendimento<br>
    é prioridade, portanto garantimos um serviço único<br>
    para os clientes.
  </p>

  <div class="brand-panel">
    <div class="brand"><span class="brand-dot"></span>Orvalis</div>
  </div>

  <div class="about-photo" role="img" aria-label="Fotografia de dois executivos de terno apertando as mãos"></div>
</body>
</html>
```